Help me design my in store poster to promote our Loan product!

We need a design for a 2 X 3 poster inside our stores to promote our installment loan product. We are called Wade's Check Cashing, but offer loans inside our stores. We are open to a new logo for Wade's Loans, and open to any new exciting colors to stand out in the store. We provide short term monthly installment loans, we have monthly payments from 3 - 12 months. Our loans range from $100 - $1,400 with low interest. We ask for ID, consistent source of income, and credit check. We help build credit, and it is fast and easy. We want it to be simple and clean to get people's attention when they are inside our stores. Please help!

UPDATE: The design will be for a 2 X 7 poster now. Less words.

Other font styles liked:
• Rounded corners with the font

Requirements
Must have
• Bold colors, the words: loans, cash, $100 - $1,400, monthly payments, credit building, quick.
Nice to have
• A new logo, the Wade's Check Cashing logo added as reference

UPDATE: If we can add a quick slogan : FAST CASH NOW or HELP IS HERE or YOUR CASH IS HERE or LOANS FOR LIVING or LOANS FOR LIFE

A WADE'S FINANCE LOGO that looks similar to the NOVAJET logo I attached.

```html
<!DOCTYPE html>
<html lang="en">
<head>
<meta charset="utf-8">
<title>Wade's Loans — In-Store Poster</title>
<link href="https://fonts.googleapis.com/css2?family=Montserrat:wght@700;800&display=swap" rel="stylesheet">
<style>
  :root {
    --navy: #0d4c9c;
    --green: #9ccb3b;
    --ink: #111111;
    --white: #ffffff;
    --photo-light: #e4e4e4;
    --photo-dark: #a8a8a8;
    --backdrop: #eef1f4;
  }
  * { margin: 0; padding: 0; box-sizing: border-box; }
  html, body {
    width: 1200px; height: 1074px; overflow: hidden;
    background: var(--backdrop);
    font-family: "Montserrat", sans-serif;
  }
  .poster {
    position: absolute; left: 255px; top: 20px;
    width: 690px; height: 1034px;
    background: var(--white);
    overflow: hidden;
  }
  .poster-shapes { position: absolute; inset: 0; }
  .text { position: absolute; left: 0; width: 100%; text-align: center; font-weight: 800; text-transform: uppercase; white-space: nowrap; }
  .navy { color: var(--navy); }
  .green { color: var(--green); }
  .white { color: var(--white); }

  .promise {
    left: 372px; width: 300px; top: 82px;
    font-size: 33px; line-height: 38px; color: var(--navy);
  }
  .brand-name {
    top: 560px; font-size: 52px; line-height: 60px; color: var(--navy);
    letter-spacing: 1px;
  }
  .product-line { top: 624px; font-size: 14px; line-height: 18px; color: var(--ink); }
  .range-intro { top: 655px; font-size: 31px; line-height: 38px; color: var(--navy); }
  .range-amount { top: 684px; font-size: 70px; line-height: 84px; color: var(--green); letter-spacing: -1px; }
  .range-note { left: 98px; width: 505px; top: 771px; font-size: 31px; line-height: 38px; color: var(--white); }
  .payments { top: 832px; font-size: 19px; line-height: 25px; color: var(--ink); }
  .requirements { top: 922px; font-size: 26px; line-height: 32px; }
</style>
</head>
<body>
  <main class="poster">
    <svg class="poster-shapes" width="690" height="1034" viewBox="0 0 690 1034">
      <defs>
        <linearGradient id="photoTone" x1="0" y1="0" x2="1" y2="1">
          <stop offset="0" stop-color="var(--photo-light)"/>
          <stop offset="1" stop-color="var(--photo-dark)"/>
        </linearGradient>
      </defs>
      <rect class="hero-photo" x="0" y="0" width="690" height="600" fill="url(#photoTone)" role="img" aria-label="Photo: a businessman in a dark suit holding out a fan of hundred-dollar bills"/>
      <circle class="promise-badge" cx="522" cy="175" r="150" fill="var(--white)"/>
      <path class="hero-band" d="M0,468 Q345,570 690,468 L690,500 Q345,600 0,500 Z" fill="var(--navy)"/>
      <path class="body-panel" d="M0,500 Q345,600 690,500 L690,1034 L0,1034 Z" fill="var(--white)"/>
      <line x1="44" y1="633" x2="95" y2="633" stroke="var(--green)" stroke-width="5"/>
      <line x1="595" y1="633" x2="646" y2="633" stroke="var(--green)" stroke-width="5"/>
      <path class="bracket" d="M94,664 H70 V795 H94" fill="none" stroke="var(--navy)" stroke-width="8"/>
      <path class="bracket" d="M603,664 H627 V795 H603" fill="none" stroke="var(--navy)" stroke-width="8"/>
      <polygon class="ribbon" points="98,766 603,766 590,790 603,814 98,814 111,790" fill="var(--navy)"/>
      <path class="footer-rule" d="M0,930 Q345,870 690,930" fill="none" stroke="var(--navy)" stroke-width="12"/>
      <path class="footer-panel" d="M0,942 Q345,882 690,942 L690,1034 L0,1034 Z" fill="var(--green)"/>
    </svg>

    <p class="text promise">We<br>help build<br><span class="green">credit,</span><br>and it is<br><span class="green">fast &amp; easy.</span></p>

    <h1 class="text brand-name">Wade's Loans</h1>

    <p class="text product-line">We provide short term <span class="navy">monthly installment</span> loans</p>
    <p class="text range-intro">Our <span class="green">loans</span> range from</p>
    <p class="text range-amount">$100 - $1,400</p>
    <p class="text range-note">With low interest.</p>
    <p class="text payments">We have <span class="navy">monthly payments</span> from<br><span class="navy">3 - 12 months.</span></p>

    <p class="text requirements"><span class="navy">We ask for ID,</span><br><span class="white">consistent source of income,</span><br><span class="navy">and credit check.</span></p>
  </main>
</body>
</html>
```